Business Card Design

The Wren Hollow Inn is the most centrally located motel in Grafton.
We are the only family owned motel in Grafton.
Our colour scheme is blue, whiteand black.

I have uploaded a photo of our new rooms and the logo for you to use Thanks. Looking good

Industry/Entity Type

Motel

Contact Information for Business Card

The Wren Hollow Inn
Marcus & Helena Dobrev
Owner/Operators
14-16 Pellham Street, Grafton NSW 2460
Ph: 02 6690 3457
Email: thewrenhollowinn@mailbox.example
reception@wrenhollowinn.example
www.wrenhollowinn.example

Colors
0392cd
0455a3

```html
<!DOCTYPE html>
<html lang="en">
<head>
<meta charset="utf-8">
<title>The Wren Hollow Inn – Business Card</title>
<link rel="stylesheet" href="https://fonts.googleapis.com/css2?family=Oswald:wght@300;400;500&display=swap">
<style>
  :root {
    --card-blue: #0b97d7;
    --brand-navy: #0455a3;
    --ink-white: #ffffff;
    --page-bg: #ffffff;
    --edge-grey: #d6d6d6;
  }
  * { margin: 0; padding: 0; box-sizing: border-box; }
  html, body {
    width: 947px;
    height: 1200px;
    overflow: hidden;
    background: var(--page-bg);
  }
  .canvas {
    position: relative;
    width: 947px;
    height: 1200px;
    display: flex;
    align-items: center;
    justify-content: center;
  }
  .business-card {
    position: relative;
    width: 900px;
    height: 500px;
    background: var(--card-blue);
    border-radius: 8px 0 34px 0;
    box-shadow: 0 0 0 1px var(--edge-grey);
    font-family: "Oswald", "Arial Narrow", sans-serif;
    color: var(--ink-white);
    text-align: center;
  }
  .brand {
    position: absolute;
    top: 52px;
    left: 0;
    right: 0;
    display: flex;
    align-items: center;
    justify-content: center;
    gap: 18px;
  }
  .brand-dot {
    width: 54px;
    height: 54px;
    border-radius: 50%;
    background: var(--brand-navy);
  }
  .brand-name {
    font-family: "Oswald", "Arial Narrow", sans-serif;
    font-weight: 500;
    font-size: 52px;
    line-height: 1;
    color: var(--brand-navy);
  }
  .owner-names {
    position: absolute;
    top: 168px;
    left: 0;
    right: 0;
    font-weight: 500;
    font-size: 72px;
    line-height: 1;
    letter-spacing: 3px;
  }
  .name-rule {
    position: absolute;
    top: 258px;
    left: 50px;
    width: 810px;
    height: 4px;
    background: var(--ink-white);
  }
  .owner-role {
    position: absolute;
    top: 285px;
    left: 0;
    right: 0;
    font-weight: 300;
    font-size: 46px;
    line-height: 1;
    letter-spacing: 13px;
  }
  .contact-list {
    position: absolute;
    top: 358px;
    left: 0;
    right: 0;
    list-style: none;
    font-weight: 400;
    line-height: 1;
  }
  .contact-list li { margin-bottom: 14px; }
  .contact-phone { font-size: 28px; letter-spacing: 1.5px; }
  .contact-email { font-size: 27px; letter-spacing: 1px; }
  .contact-address { font-size: 25px; letter-spacing: 1px; margin-top: 14px; }
</style>
</head>
<body>
<main class="canvas">
  <section class="business-card" aria-label="Business card for The Wren Hollow Inn">
    <div class="brand">
      <span class="brand-dot" aria-hidden="true"></span>
      <span class="brand-name">The Wren Hollow Inn</span>
    </div>
    <h1 class="owner-names">Marcus &amp; Helena Dobrev</h1>
    <div class="name-rule" aria-hidden="true"></div>
    <p class="owner-role">Owner/Operators</p>
    <ul class="contact-list">
      <li class="contact-phone">Contact Ph: 02 6690 3457</li>
      <li class="contact-email">Email: thewrenhollowinn@mailbox.example</li>
      <li class="contact-address">14-16 Pellham Street, Grafton NSW 2460</li>
    </ul>
  </section>
</main>
</body>
</html>
```